The Vigor Depot needs a postcard design.

We need a postcard design for our new retail/consignment store called "The Vigor Depot". We buy, sell and consign gently used exercise equipment. We offer treadmills, ellipticals, gyms, bikes and more. We can save our customers up to 50% off retail prices. We also offer delivery, set-up, removal/recycling of old equipment, and repair. Our initial product/business (and formerly store name) is RoadWell Gym Service - our mobile business that offers repairs & service/maintenance. We would like this postcard to focus only on The Vigor Depot and be bright, colorful and cheerful, inviting the community to come in and see how we can fit them with the right piece of equipment both physically and economically.
We specialize in buying, selling and consigning pre-owned equipment.

The overall design should be informative about who we are, what we offer, and one that communicates we are inviting them to stop by and check us out.

Thank you!!

Target Market(s)

People wanting to work out at home on a budget.
The elderly, rehab patients, moms wanting pre-baby body back,
health conscience people as well as appeal the the younger crowd.

Industry/Entity Type

Fitness Equipment

Font styles to use
Serif

Colors
3276b5
33a6d7
0393ce
33b8a4
add136
fbee3d
ffcf3e
faa54b

Requirements
Must have
• our logo, address: 4870 Birch Ln. SE Salem, Or 97306, phone #: 971-555-0187
• lots of color-
• Caption of " Save up to 50% off of retail prices
• "We deliver" "Delivery Available"
Nice to have
• We like the design idea of layering images, transparent images in the background and the use of lots of color that engages the potential customer.
• Website or QR code - www.thevigordepot-example.net
Should not have
• Realistic images of people or exercise equipment. Should not be tailored after our RoadWell website. This is a completely different business. We want to stay away from the red/black color scheme. Also should not mention "NEW". We do not want the focus to be on new equipment.

```html
<!DOCTYPE html>
<html lang="en">
<head>
<meta charset="utf-8">
<title>The Vigor Depot Postcard</title>
<link href="https://fonts.googleapis.com/css2?family=Oswald:wght@500;700&family=Lato:wght@400;700;900&display=swap" rel="stylesheet">
<style>
  :root {
    --stage: #2a2a2a;
    --white: #ffffff;
    --blue: #2f78c0;
    --blue-dark: #1f5fa3;
    --sky: #33a6d7;
    --orange: #f6a623;
    --green: #7cc242;
    --grey-text: #555a60;
    --body-text: #3a3f46;
    --line: #c9c9c9;
  }
  * { margin: 0; padding: 0; box-sizing: border-box; }
  html, body { width: 806px; height: 1200px; overflow: hidden; background: var(--stage); }
  body { position: relative; font-family: "Lato", Arial, sans-serif; }

  .postcard { position: absolute; width: 652px; height: 507px; background: var(--white); overflow: hidden; }
  .postcard--front { left: 76px; top: 70px; }
  .postcard--back { left: 73px; top: 625px; width: 653px; height: 505px; }
  .postcard svg.shapes { position: absolute; inset: 0; }
  .abs { position: absolute; }

  .brand { left: 40px; top: 42px; width: 290px; display: flex; align-items: center; gap: 12px; }
  .brand-dot { width: 30px; height: 30px; border-radius: 50%; background: var(--blue); }
  .brand-name { font-weight: 900; font-size: 30px; color: var(--blue); white-space: nowrap; }

  .save-lead { left: 0; width: 340px; top: 180px; text-align: center; font-weight: 900; font-size: 16.5px; color: #4a6f98; white-space: nowrap; }
  .save-big { left: 0; width: 340px; top: 196px; text-align: center; font-family: "Oswald", sans-serif; font-weight: 700; font-size: 44px; line-height: 1.2; color: var(--blue); white-space: nowrap; }
  .save-tail { left: 0; width: 340px; top: 250px; text-align: center; font-size: 25px; color: var(--grey-text); letter-spacing: 0.5px; white-space: nowrap; }

  .badge { width: 84px; height: 84px; border-radius: 50%; background: var(--white); border: 5px solid var(--blue); display: flex; flex-direction: column; align-items: center; justify-content: center; text-align: center; }
  .badge svg { width: 20px; height: 20px; margin-bottom: 2px; }
  .badge-title { font-weight: 900; font-size: 11px; line-height: 1.05; color: var(--blue); }
  .badge-sub { font-weight: 700; font-size: 10px; line-height: 1.05; color: var(--green); }
  .badge-note { font-size: 4px; color: var(--green); }

  .address { left: 20px; top: 413px; font-size: 15px; color: var(--grey-text); font-weight: 700; display: flex; align-items: center; gap: 4px; white-space: nowrap; }
  .hours { left: 40px; top: 433px; font-size: 14.5px; font-weight: 700; color: var(--blue); }
  .contact { left: 20px; top: 455px; display: flex; align-items: center; gap: 6px; white-space: nowrap; }
  .contact .phone { font-weight: 900; font-size: 20px; color: var(--blue); margin-right: 6px; }
  .contact .web { font-weight: 700; font-size: 12px; color: var(--blue); }

  .headline { left: 412px; top: 40px; width: 230px; text-align: center; }
  .headline .line1 { font-family: "Oswald", sans-serif; font-weight: 700; font-size: 42px; color: var(--blue); line-height: 1; }
  .headline .line2 { font-weight: 700; font-size: 26px; color: #7a7c80; letter-spacing: 0.5px; margin-top: 4px; }

  .about-title { left: 16px; top: 32px; font-family: "Oswald", sans-serif; font-weight: 700; font-size: 27px; color: var(--blue); display: flex; align-items: center; gap: 8px; }
  .about-title .dash { display: flex; flex-direction: column; gap: 4px; }
  .about-title .dash span { display: block; height: 3px; background: var(--sky); }
  .about-text { left: 16px; top: 75px; width: 300px; font-weight: 700; font-size: 15px; line-height: 1.14; color: var(--body-text); }
  .back-phone { left: 30px; top: 383px; display: flex; align-items: center; gap: 6px; font-weight: 900; font-size: 25px; color: var(--white); white-space: nowrap; }
  .back-web { left: 30px; top: 419px; display: flex; align-items: center; gap: 10px; font-weight: 700; font-size: 11px; color: var(--body-text); white-space: nowrap; }
</style>
</head>
<body>

<section class="postcard postcard--front">
  <svg class="shapes" width="652" height="507" viewBox="0 0 652 507">
    <defs>
      <linearGradient id="orangeFront" x1="0" y1="0" x2="0" y2="1">
        <stop offset="0" stop-color="#f7a51f"/>
        <stop offset="0.6" stop-color="#ffcc3a"/>
        <stop offset="1" stop-color="#ffe05c"/>
      </linearGradient>
      <linearGradient id="peachTop" x1="0" y1="0" x2="0" y2="1">
        <stop offset="0" stop-color="#fbd79a"/>
        <stop offset="1" stop-color="#fde9c4"/>
      </linearGradient>
      <linearGradient id="photoFront" x1="0" y1="0" x2="1" y2="1">
        <stop offset="0" stop-color="#a3a09a"/>
        <stop offset="0.5" stop-color="#7f8285"/>
        <stop offset="1" stop-color="#55585c"/>
      </linearGradient>
      <clipPath id="rightPanel">
        <path d="M414 0 Q283 250 444 507 L652 507 L652 0 Z"/>
      </clipPath>
    </defs>
    <rect width="652" height="507" fill="#f5f5f5"/>
    <rect x="0" y="126" width="652" height="8" fill="var(--blue)"/>
    <rect x="0" y="138" width="652" height="248" fill="url(#orangeFront)"/>
    <rect x="0" y="357" width="652" height="10" fill="var(--blue)"/>
    <rect x="0" y="386" width="652" height="121" fill="var(--white)"/>
    <g clip-path="url(#rightPanel)">
      <rect x="260" y="0" width="392" height="507" fill="url(#peachTop)"/>
      <rect x="260" y="132" width="392" height="375" fill="url(#photoFront)" role="img" aria-label="Photo of a used treadmill on the showroom floor"/>
    </g>
    <path d="M414 0 Q283 250 444 507" fill="none" stroke="var(--white)" stroke-width="14"/>
    <path d="M404 0 Q273 250 434 507" fill="none" stroke="var(--blue)" stroke-width="8"/>
    <path d="M420 0 Q289 250 452 507" fill="none" stroke="var(--blue-dark)" stroke-width="4"/>
  </svg>

  <div class="abs brand"><span class="brand-dot"></span><span class="brand-name">The Vigor Depot</span></div>

  <div class="abs save-lead">WE CAN SAVE OUR CUSTOMERS</div>
  <div class="abs save-big">UP TO 50% OFF</div>
  <div class="abs save-tail">RETAIL PRICES</div>

  <div class="abs badge" style="left:31px;top:310px;">
    <svg viewBox="0 0 20 20"><circle cx="10" cy="11" r="8" fill="var(--green)"/><text x="10" y="15" font-size="11" font-weight="900" text-anchor="middle" fill="#fff" font-family="Lato">$</text></svg>
    <div class="badge-title">CASH FOR</div>
    <div class="badge-sub">YOURS</div>
  </div>
  <div class="abs badge" style="left:129px;top:310px;">
    <svg viewBox="0 0 20 20"><path d="M3 10 L8 15 L17 4" fill="none" stroke="var(--green)" stroke-width="3"/></svg>
    <div class="badge-title">30 DAYS</div>
    <div class="badge-sub">WARRANTY</div>
    <div class="badge-note">ASK FOR DETAILS</div>
  </div>
  <div class="abs badge" style="left:230px;top:310px;">
    <svg viewBox="0 0 20 20"><path d="M10 19 C4 12 3 9 3 7 a7 7 0 0 1 14 0 c0 2 -1 5 -7 12z" fill="none" stroke="var(--green)" stroke-width="2"/><circle cx="10" cy="7" r="2.3" fill="var(--green)"/></svg>
    <div class="badge-title">CONSIGN</div>
    <div class="badge-sub">E-MADE<br>E-Z</div>
  </div>

  <div class="abs address">
    <svg width="16" height="15" viewBox="0 0 16 15"><path d="M1 8 L8 1 L15 8 M3 6 V14 H13 V6" fill="none" stroke="var(--sky)" stroke-width="1.8"/></svg>
    4870 Birch Ln. SE Salem, Or 97306
  </div>
  <div class="abs hours">Tues-Sat 10:30-5pm</div>
  <div class="abs contact">
    <svg width="16" height="16" viewBox="0 0 16 16"><rect width="16" height="16" rx="3" fill="var(--green)"/><path d="M5 3 L7 6 L6 7.5 Q7 10 8.5 10.5 L10 9.5 L13 11.5 L12 13 Q6 13 3 5 Z" fill="#fff"/></svg>
    <span class="phone">971-555-0187</span>
    <svg width="12" height="12" viewBox="0 0 12 12"><circle cx="6" cy="6" r="5" fill="none" stroke="var(--green)"/><path d="M1 6 H11 M6 1 Q3 6 6 11 Q9 6 6 1" fill="none" stroke="var(--green)"/></svg>
    <span class="web">www.thevigordepot-example.net</span>
  </div>

  <div class="abs headline">
    <div class="line1">GOOD DEALS</div>
    <div class="line2">FINALLY HERE</div>
  </div>
</section>

<section class="postcard postcard--back">
  <svg class="shapes" width="653" height="505" viewBox="0 0 653 505">
    <defs>
      <linearGradient id="orangeBack" x1="0" y1="0" x2="0" y2="1">
        <stop offset="0" stop-color="#f7a51f"/>
        <stop offset="0.5" stop-color="#ffc93a"/>
        <stop offset="1" stop-color="#ffe15e"/>
      </linearGradient>
    </defs>
    <rect width="653" height="505" fill="var(--white)"/>
    <path d="M0 0 H300 Q420 240 282 505 H0 Z" fill="url(#orangeBack)"/>
    <path d="M308 0 Q428 240 290 505" fill="none" stroke="var(--blue)" stroke-width="8"/>
    <path d="M322 0 Q442 240 304 505" fill="none" stroke="var(--blue-dark)" stroke-width="4"/>
    <rect x="0" y="204" width="356" height="9" fill="var(--blue)"/>
    <rect x="0" y="330" width="356" height="9" fill="var(--blue)"/>
    <rect x="0" y="215" width="102" height="113" fill="#6f7478" role="img" aria-label="Photo of used elliptical machines"/>
    <rect x="107" y="215" width="128" height="113" fill="#8a7a66" role="img" aria-label="Photo of exercise bikes in the store"/>
    <rect x="241" y="215" width="111" height="113" fill="#d8d8d6" role="img" aria-label="Photo of an elliptical trainer console"/>
    <rect x="552" y="42" width="81" height="81" fill="none" stroke="#222" stroke-width="1.5"/>
    <line x1="407" y1="156" x2="636" y2="156" stroke="var(--line)" stroke-width="1.5"/>
    <line x1="407" y1="192" x2="636" y2="192" stroke="var(--line)" stroke-width="1.5"/>
    <line x1="407" y1="226" x2="636" y2="226" stroke="var(--line)" stroke-width="1.5"/>
  </svg>

  <div class="abs about-title">About Us
    <span class="dash"><span style="width:34px"></span><span style="width:70px;background:var(--green)"></span></span>
  </div>
  <p class="abs about-text">We buy, sell and consign gently used exercise equipment. We offer treadmills, ellipticals, gyms, bikes and more. We also offer delivery, set-up, removal/recycling of old equipment, and repair.</p>

  <div class="abs back-phone">
    <svg width="22" height="22" viewBox="0 0 16 16"><rect width="16" height="16" rx="3" fill="#fff"/><path d="M5 3 L7 6 L6 7.5 Q7 10 8.5 10.5 L10 9.5 L13 11.5 L12 13 Q6 13 3 5 Z" fill="var(--orange)"/></svg>
    971-555-0187
  </div>
  <div class="abs back-web">
    <svg width="12" height="12" viewBox="0 0 12 12"><circle cx="6" cy="6" r="5" fill="none" stroke="var(--blue)"/><path d="M1 6 H11 M6 1 Q3 6 6 11 Q9 6 6 1" fill="none" stroke="var(--blue)"/></svg>
    www.thevigordepot-example.net
  </div>
</section>

</body>
</html>
```